Business Card Design Project

Need a business card designed for a horse racing/gambling centered company.
Company name is BrightQuill.com.au
Company colours are similar to those in the logo.
Something clean and modern , designer given liberty to be creative.
Incorporate the logo is preferred.
Single or Double Sided fine
Must include :
Name
Mobile Number
Email Address
Reason: Apologies, I have been traveling unexpectedly with business and just need the extra two days to reply and give feedback before making a decision.
Industry/Entity Type
Business

```html
<!DOCTYPE html>
<html lang="en">
<head>
<meta charset="utf-8">
<title>BrightQuill.com.au Business Card</title>
<link rel="stylesheet" href="https://fonts.googleapis.com/css2?family=Crimson+Text:wght@400;600&display=swap">
<style>
  :root {
    --page-bg: #ecebe8;
    --teal: #22ad9d;
    --teal-deep: #16978a;
    --teal-light: #3cc2b2;
    --card-white: #ffffff;
    --text-grey: #8a8a8a;
    --text-dark: #6f6f6f;
    --check-grey: #e4e4e6;
  }
  * { box-sizing: border-box; margin: 0; padding: 0; }
  html, body {
    width: 1200px; height: 900px; overflow: hidden;
    background: var(--page-bg);
    font-family: "Crimson Text", Georgia, serif;
  }
  .sheet {
    width: 1200px; height: 900px;
    display: flex; flex-direction: column;
    align-items: center; justify-content: center; gap: 50px;
  }
  .card {
    position: relative;
    width: 630px; height: 360px;
    border-radius: 4px;
    overflow: hidden;
    box-shadow: 0 6px 18px rgba(0,0,0,0.14);
  }
  /* Front */
  .card-front {
    background: linear-gradient(160deg, var(--teal-light) 0%, var(--teal) 45%, var(--teal-deep) 100%);
  }
  .front-checker-band {
    position: absolute; top: 0; right: 0;
    width: 34px; height: 100%;
    background: linear-gradient(180deg, rgba(255,255,255,0.75), rgba(255,255,255,0.35));
  }
  .brand-lockup {
    position: absolute; left: 70px; top: 50%;
    transform: translateY(-50%);
    display: flex; align-items: center; gap: 18px;
  }
  .brand-dot {
    width: 34px; height: 34px; border-radius: 50%;
    background: var(--card-white);
  }
  .brand-name {
    color: var(--card-white);
    font-size: 40px; font-weight: 600;
    letter-spacing: 0.5px;
  }
  /* Back */
  .card-back { background: var(--card-white); }
  .back-checker-band {
    position: absolute; top: 0; left: 0;
    width: 36px; height: 100%;
    background: linear-gradient(180deg, var(--teal) 0%, #9ed9d1 50%, var(--teal) 100%);
  }
  .back-faint-pattern {
    position: absolute; top: 0; right: 0;
    width: 300px; height: 200px;
    background: radial-gradient(ellipse at top right, var(--check-grey) 0%, rgba(228,228,230,0.4) 50%, rgba(255,255,255,0) 80%);
  }
  .contact-block {
    position: absolute; left: 90px; top: 74px;
  }
  .contact-site {
    color: var(--text-grey);
    font-size: 30px; font-weight: 400;
    margin-bottom: 30px;
  }
  .contact-list {
    list-style: none;
    color: var(--text-dark);
    font-size: 20px;
    margin-left: 34px;
  }
  .contact-list li {
    position: relative;
    margin-bottom: 26px;
  }
  .contact-list li::before {
    content: "";
    position: absolute; left: -22px; top: 11px;
    width: 6px; height: 6px; border-radius: 50%;
    background: var(--text-dark);
  }
</style>
</head>
<body>
  <main class="sheet">
    <section class="card card-front">
      <div class="brand-lockup">
        <span class="brand-dot"></span>
        <span class="brand-name">BrightQuill.com.au</span>
      </div>
      <div class="front-checker-band" role="img" aria-label="Checkered flag band in white and teal"></div>
    </section>

    <section class="card card-back">
      <div class="back-faint-pattern" role="img" aria-label="Faint grey checkered flag pattern"></div>
      <div class="back-checker-band" role="img" aria-label="Checkered flag band in teal and white"></div>
      <div class="contact-block">
        <p class="contact-site">BrightQuill.com.au</p>
        <ul class="contact-list">
          <li class="contact-name">Liam Porter</li>
          <li class="contact-phone">0498365127</li>
          <li class="contact-email">liam@brightquill.com.au</li>
        </ul>
      </div>
    </section>
  </main>
</body>
</html>
```